Product Menu 8 x 11- Home Inspection Company Ancillary Services

Hello, on the front side of the flyer will be all about sewer camera inspections. These will include the images of the damages on the front and the information on the Sewer Scope Inspections: Safeguard Your Home from Hidden Plumbing Issues.
On the back will include indoor air quality. Solar Panel Inspections, Roof Certifications, and Expert Raised Foundation Review.
Please use logo and colors as a branding guide for the flyer.
$275- Sewer Camera Fee
$495 -Indoor Air Quality Inspection- Getting an indoor air quality (IAQ) inspection for mold when buying a home is crucial for health, safety, and financial protection. Mold can cause serious respiratory issues, especially for those with allergies or asthma, and toxic molds like black mold pose additional risks. It often grows in hidden areas, such as behind walls or in HVAC systems, often linked to water damage or structural issues. Early detection allows you to negotiate remediation costs, prevent mold from spreading, and avoid expensive repairs, ensuring a safe and sound investment.
$395 -Solar Panel Inspection- Getting a solar panel inspection when buying a home is essential to ensure efficiency, safety, and long-term savings. It verifies the system’s condition, identifying issues like damaged panels, faulty wiring, or inefficient inverters that could impact performance or pose safety risks. The inspection also evaluates the system’s energy output and compatibility with your energy needs, ensuring you’re benefiting from the investment. Additionally, understanding the age, warranty, and maintenance history of the system helps avoid unexpected repair costs and maximizes the value of this eco-friendly feature.
$399 Roof Certifications- Obtaining a roof certification when buying a home is vital for assessing the roof's condition, lifespan, and potential repair needs. This certification provides a professional evaluation, ensuring the roof is free from leaks, damage, or structural issues, which could lead to costly repairs. Many insurance companies require a roof certification before issuing or renewing a policy, particularly for older roofs, to confirm it meets safety standards. Having this certification not only provides peace of mind but also helps facilitate insurance coverage and protects your investment in the property.
$199- Advanced Foundation Review-An advanced foundation review by a licensed foundation contractor is essential when buying a home, as it provides a detailed assessment beyond what a general home inspector can offer. While home inspectors are trained generalists who identify visible issues, a foundation contractor is a specialist with the expertise to evaluate structural integrity, detect hidden problems, and determine the severity of any concerns. This specialized review can uncover issues like uneven settling, cracks, or drainage problems that may require repairs, ensuring you have a clear understanding of the foundation's condition before making a significant investment.
Real Estate Buyers and Real Estate Agents

```html
<!DOCTYPE html>
<html lang="en">
<head>
<meta charset="utf-8">
<title>Summit Crest – Ancillary Services Flyer</title>
<link href="https://fonts.googleapis.com/css2?family=Montserrat:wght@400;500;600;700;800;900&display=swap" rel="stylesheet">
<style>
:root{
  --blue:#1769c2;
  --blue-dark:#0f4f9a;
  --red:#d7282f;
  --ink:#333;
  --footer-dark:#3b3b3d;
  --stage:#939393;
  --white:#fff;
}
*{box-sizing:border-box;margin:0;padding:0}
html,body{width:1200px;height:817px;overflow:hidden}
body{background:var(--stage);font-family:'Montserrat',sans-serif;color:var(--ink);position:relative}
.page{position:absolute;top:63px;width:661px;height:854px;background:var(--white);transform:scale(.8);transform-origin:0 0;overflow:hidden;box-shadow:0 2px 6px rgba(0,0,0,.25)}
.page--front{left:52px}
.page--back{left:618px}
.abs{position:absolute}
.shapes{position:absolute;left:0;top:0}

/* brand */
.brand{position:absolute;width:150px;text-align:center}
.brand__dot{width:58px;height:58px;border-radius:50%;background:var(--blue);border:4px solid var(--red);margin:0 auto 6px}
.brand__name{font-weight:800;font-size:13px;color:var(--red);letter-spacing:.5px}
.brand__tag{font-size:4.5px;color:var(--blue);font-weight:600;letter-spacing:.4px}

/* front hero */
.hero-title{left:63px;top:130px;color:var(--white);font-weight:900;line-height:.92}
.hero-title .big{display:block;font-size:54px;letter-spacing:1px}
.hero-title .mid{display:block;font-size:31px;margin-top:6px;letter-spacing:.5px}
.hero-sub{left:62px;top:270px;color:var(--white);font-weight:700;font-size:17px;line-height:22px}
.photo{background:linear-gradient(160deg,#8b8d8f,#4d4a45 60%,#2a2725)}
.badge{position:absolute;width:62px;height:62px;border-radius:50%;border:4px solid #fff;box-shadow:0 0 0 2px #bbb}

.price-burst{position:absolute;text-align:center;color:var(--white);font-weight:800}
.price-burst svg{position:absolute;left:0;top:0}
.price-burst span{position:relative;display:block}

.whatis{left:340px;top:307px;width:265px}
.whatis h2{font-size:13.5px;font-weight:500;line-height:16px;color:var(--ink)}
.whatis h2 strong{display:block;color:var(--blue);font-weight:700}
.whatis p{font-size:9.4px;line-height:11.7px;margin-top:6px}

.shot{position:absolute;top:418px;width:172px;border:1px solid #ccc;background:#fff}
.shot__img{height:104px}
.shot__cap{font-size:8px;font-weight:700;text-align:center;line-height:10px;letter-spacing:-.2px;padding:0 3px;height:32px;display:flex;align-items:center;justify-content:center;color:#222}

.why{left:36px;top:582px;width:588px;height:216px;border:1.5px solid var(--blue)}
.tab{position:absolute;height:24px;background:var(--blue);color:var(--white);font-size:14px;text-align:center;line-height:24px;white-space:nowrap;clip-path:polygon(12px 0,calc(100% - 12px) 0,100% 100%,0 100%)}
.tab strong{font-weight:700}
.card{position:absolute;top:607px;width:103px;height:170px;border:1px solid var(--blue);border-radius:0 0 6px 6px;background:#fff}
.card__head{height:42px;color:#fff;font-weight:700;font-size:10px;line-height:11px;text-align:center;padding-top:12px}
.card--blue .card__head{background:var(--blue)}
.card--red .card__head{background:var(--red)}
.card--red{border-color:var(--red)}
.card__icon{position:absolute;left:38px;top:-13px;width:26px;height:26px;border-radius:50%;background:#fff;border:2px solid var(--red)}
.card__icon::after{content:"";position:absolute;left:6px;top:6px;width:10px;height:10px;border:1.5px solid var(--red);border-radius:2px}
.card p{font-size:7.1px;line-height:8.6px;text-align:center;padding:5px 5px}

.cta{position:absolute;left:0;width:661px;text-align:center;font-size:15px;font-weight:500;color:#333}
.cta strong{color:var(--blue);font-weight:800}
.cta::before,.cta::after{content:"";display:inline-block;width:34px;height:1px;background:#999;vertical-align:middle;margin:0 8px}

/* footer */
.footer{position:absolute;left:0;top:812px;width:661px;height:42px;background:var(--footer-dark);color:#fff}
.footer__red{position:absolute;left:0;top:0;width:232px;height:42px;background:var(--red);clip-path:polygon(0 0,212px 0,232px 100%,0 100%)}
.footer__phone{position:absolute;left:66px;top:9px;font-size:18px;font-weight:700;display:flex;align-items:center;gap:6px}
.ico{display:inline-block;width:15px;height:15px;border-radius:50%;background:#fff;position:relative;flex:none}
.ico--phone{background:#fff}
.ico--phone::after{content:"";position:absolute;left:4px;top:3px;width:6px;height:8px;border-left:2.5px solid var(--blue);border-bottom:2.5px solid var(--blue);border-radius:0 0 0 4px}
.ico--red{background:var(--red);width:11px;height:11px}
.footer__addr{position:absolute;left:236px;top:10px;font-size:8.8px;line-height:10.5px;display:flex;gap:6px}
.footer__mail{position:absolute;left:405px;top:10px;font-size:8.8px;line-height:11px}
.footer__mail div{display:flex;gap:6px;align-items:center}

/* back page */
.back-title{left:258px;top:22px;color:#fff;font-weight:800;font-size:30px;line-height:33px;letter-spacing:.3px}
.service{position:absolute;left:66px;width:531px;height:125px;border:1.5px solid var(--blue);border-radius:6px}
.service p{position:absolute;font-size:8.2px;line-height:10.3px;color:#333}
.service .photo{position:absolute;border-radius:4px}
</style>
</head>
<body>

<svg width="0" height="0" style="position:absolute">
  <defs>
    <symbol id="burst" viewBox="0 0 100 100">
      <circle cx="50" cy="50" r="44" fill="#d7282f"/>
      <circle cx="50" cy="50" r="46" fill="none" stroke="#d7282f" stroke-width="8" stroke-dasharray="4.2 3.1"/>
      <circle cx="50" cy="50" r="38" fill="none" stroke="#fff" stroke-width=".8" stroke-dasharray="1.5 1.5"/>
    </symbol>
  </defs>
</svg>

<!-- FRONT -->
<section class="page page--front">
  <svg class="shapes" width="661" height="400" viewBox="0 0 661 400">
    <defs>
      <linearGradient id="pipe" x1="0" y1="0" x2="0.3" y2="1">
        <stop offset="0" stop-color="#a29d95"/><stop offset=".5" stop-color="#5b4a3a"/><stop offset="1" stop-color="#2e2620"/>
      </linearGradient>
      <clipPath id="pipeClip"><polygon points="365,0 661,0 661,276 430,276 400,250 358,140"/></clipPath>
    </defs>
    <polygon points="360,0 661,0 661,276 430,276 395,250 355,140" fill="#5a5650"/>
    <rect role="img" aria-label="Camera view inside a sewer pipe with tree root intrusion" x="360" y="0" width="301" height="276" fill="url(#pipe)" clip-path="url(#pipeClip)"/>
    <polyline points="365,-2 298,81" stroke="#d7282f" stroke-width="6" fill="none"/>
    <polygon points="0,81 300,81 352,170 300,327 0,327" fill="#1769c2"/>
    <polyline points="300,81 360,178 306,330" stroke="#fff" stroke-width="6" fill="none"/>
    <polyline points="312,78 370,178 316,332" stroke="#d7282f" stroke-width="5" fill="none"/>
  </svg>

  <div class="brand" style="left:98px;top:18px">
    <div class="brand__dot"></div>
    <div class="brand__name">SUMMIT CREST</div>
    <div class="brand__tag">INSPECTION PROFESSIONALS</div>
  </div>

  <h1 class="abs hero-title"><span class="big">SEWER<br>SCOPE</span><span class="mid">INSPECTIONS</span></h1>
  <p class="abs hero-sub">Safeguard Your Home from<br>Hidden Plumbing Issues</p>

  <div class="badge" style="left:70px;top:334px;background:var(--red)"></div>
  <div class="badge" style="left:143px;top:334px;background:#c9a227"></div>
  <div class="badge" style="left:215px;top:334px;background:#8a8a8a"></div>

  <div class="price-burst" style="left:405px;top:166px;width:140px;height:140px">
    <svg width="140" height="140"><use href="#burst"/></svg>
    <span style="padding-top:28px;font-size:12px;line-height:12px">SEWER<br>CAMERA</span>
    <span style="font-size:22px;line-height:24px">FEE</span>
    <span style="font-size:31px;line-height:30px;color:#ffe46b"><sup style="font-size:14px">$</sup>275</span>
  </div>

  <div class="abs whatis">
    <h2>WHAT IS A <strong>SEWER SCOPE INSPECTION?</strong></h2>
    <p>A sewer scope inspection uses a camera to inspect your home's sewer lines. The camera is inserted into the sewer pipe, allowing an inspector to detect blockages, cracks, tree root intrusions, and other issues that can cause significant damage if left unaddressed.</p>
  </div>

  <figure class="shot" style="left:63px">
    <div class="shot__img photo" role="img" aria-label="Sewer camera still showing root intrusion in the pipe"></div>
    <figcaption class="shot__cap">Root intrusion present in Black ABS section of sewer line at 53 feet.</figcaption>
  </figure>
  <figure class="shot" style="left:242px">
    <div class="shot__img photo" role="img" aria-label="Sewer camera still showing debris and a clog"></div>
    <figcaption class="shot__cap">Debris and clog in sewer line at 71 feet.</figcaption>
  </figure>
  <figure class="shot" style="left:421px">
    <div class="shot__img photo" role="img" aria-label="Sewer camera still showing a clog in the line"></div>
    <figcaption class="shot__cap">Clog in sewer line at 72 feet.</figcaption>
  </figure>

  <div class="abs why"></div>
  <div class="tab" style="left:112px;top:563px;width:420px">WHY YOU SHOULD GET <strong>A SEWER SCOPE INSPECTION</strong></div>

  <article class="card card--blue" style="left:67px">
    <div class="card__icon"></div>
    <h3 class="card__head">Prevent Costly<br>Repairs</h3>
    <p>Sewer line issues can be extremely expensive to fix, with some repairs costing thousands of dollars. A sewer scope inspection can identify problems early, potentially saving you from dealing with costly repairs down the road.</p>
  </article>
  <article class="card card--red" style="left:175px">
    <div class="card__icon"></div>
    <h3 class="card__head">Protect Your<br>Investment</h3>
    <p>Whether you're buying or selling a home, understanding the condition of the sewer system can impact your decision. For buyers, it helps avoid unexpected expenses. For sellers, it can provide peace of mind and ensure the sale goes smoothly.</p>
  </article>
  <article class="card card--blue" style="left:282px">
    <div class="card__icon"></div>
    <h3 class="card__head">Catch Hidden<br>Problems</h3>
    <p>Sewer line issues often remain hidden until it's too late. Without a sewer scope inspection, it's nearly impossible to identify problems that could lead to sewage backups, unpleasant odors, and costly damages.</p>
  </article>
  <article class="card card--red" style="left:389px">
    <div class="card__icon"></div>
    <h3 class="card__head">Avoid Health<br>Hazards</h3>
    <p>Faulty sewer systems can lead to sewage backups, which are not only unpleasant but also pose serious health risks. Inspections help ensure your home's plumbing is functioning safely.</p>
  </article>
  <article class="card card--blue" style="left:496px">
    <div class="card__icon"></div>
    <h3 class="card__head">Ensure Proper<br>Functioning</h3>
    <p>A sewer scope inspection gives you a better understanding of how well your sewer system is functioning. It helps detect potential issues like blockages from tree roots, misaligned pipes, or wear and tear that may cause drainage problems.</p>
  </article>

  <p class="cta" style="top:785px">GET A QUOTE OR <strong>SCHEDULE AN INSPECTION TODAY!</strong></p>

  <footer class="footer">
    <div class="footer__red"></div>
    <div class="footer__phone"><span class="ico ico--phone"></span>(555) 014-2280</div>
    <div class="footer__addr"><span class="ico ico--red"></span><span>1200 Example Blvd Ste 300<br>Springdale, CA 90000</span></div>
    <div class="footer__mail"><div><span class="ico ico--red"></span>service@summitcrestinspect.com</div><div><span class="ico ico--red"></span>summitcrestinspect.com</div></div>
  </footer>
</section>

<!-- BACK -->
<section class="page page--back">
  <svg class="shapes" width="661" height="120" viewBox="0 0 661 120">
    <polygon points="245,0 661,0 661,105 198,105" fill="#d7282f"/>
    <polyline points="232,-2 182,112 0,112" stroke="#1769c2" stroke-width="5" fill="none"/>
  </svg>
  <div class="brand" style="left:42px;top:18px">
    <div class="brand__dot"></div>
    <div class="brand__name">SUMMIT CREST</div>
    <div class="brand__tag">INSPECTION PROFESSIONALS</div>
  </div>
  <h1 class="abs back-title">HOME INSPECTION<br>ANCILLARY SERVICES</h1>

  <!-- IAQ -->
  <section class="service" style="top:151px">
    <p style="left:63px;top:18px;width:296px">Getting an indoor air quality (IAQ) inspection for mold when buying a home is crucial for health, safety, and financial protection. Mold can cause serious respiratory issues, especially for those with allergies or asthma, and toxic molds like black mold pose additional risks. It often grows in hidden areas, such as behind walls or in HVAC systems, often linked to water damage or structural issues. Early detection allows you to negotiate remediation costs, prevent mold from spreading, and avoid expensive repairs, ensuring a safe and sound investment.</p>
    <div class="photo" role="img" aria-label="Inspector operating an air quality testing device" style="left:386px;top:3px;width:142px;height:116px;background:linear-gradient(135deg,#cfd3d2,#3c3f42 55%,#1f2224)"></div>
  </section>
  <div class="tab" style="left:122px;top:136px;width:296px">INDOOR <strong>AIR QUALITY INSPECTION</strong></div>
  <div class="price-burst" style="left:45px;top:172px;width:78px;height:78px">
    <svg width="78" height="78"><use href="#burst"/></svg><span style="padding-top:23px;font-size:22px"><sup style="font-size:11px">$</sup>495</span>
  </div>

  <!-- Solar -->
  <section class="service" style="top:310px">
    <div class="photo" role="img" aria-label="House roof with solar panels and a backyard pool" style="left:4px;top:3px;width:150px;height:118px;background:linear-gradient(180deg,#8fb7e0,#6d7c8c 45%,#c9b79a 75%,#7fb1c7)"></div>
    <p style="left:162px;top:15px;width:300px">Solar Panel Inspection- Getting a solar panel inspection when buying a home is essential to ensure efficiency, safety, and long-term savings. It verifies the system's condition, identifying issues like damaged panels, faulty wiring, or inefficient inverters that could impact performance or pose safety risks. The inspection also evaluates the system's energy output and compatibility with your energy needs, ensuring you're benefiting from the investment. Additionally, understanding the age, warranty, and maintenance history of the system helps avoid unexpected repair costs and maximizes the value of this eco-friendly feature.</p>
  </section>
  <div class="tab" style="left:210px;top:292px;width:245px">SOLAR PANEL <strong>INSPECTION</strong></div>
  <div class="price-burst" style="left:553px;top:331px;width:78px;height:78px">
    <svg width="78" height="78"><use href="#burst"/></svg><span style="padding-top:23px;font-size:22px"><sup style="font-size:11px">$</sup>395</span>
  </div>

  <!-- Roof -->
  <section class="service" style="top:473px">
    <p style="left:63px;top:14px;width:312px">Roof Certifications- Obtaining a roof certification when buying a home is vital for assessing the roof's condition, lifespan, and potential repair needs. This certification provides a professional evaluation, ensuring the roof is free from leaks, damage, or structural issues, which could lead to costly repairs. Many insurance companies require a roof certification before issuing or renewing a policy, particularly for older roofs, to confirm it meets safety standards. Having this certification not only provides peace of mind but also helps facilitate insurance coverage and protects your investment in the property.</p>
    <div class="photo" role="img" aria-label="Inspector kneeling on a tiled roof" style="left:384px;top:3px;width:144px;height:118px;background:linear-gradient(160deg,#6f9b4c,#8a8f90 45%,#5e6468)"></div>
  </section>
  <div class="tab" style="left:112px;top:455px;width:218px"><strong>ROOF CERTIFICATIONS</strong></div>
  <div class="price-burst" style="left:45px;top:498px;width:78px;height:78px">
    <svg width="78" height="78"><use href="#burst"/></svg><span style="padding-top:23px;font-size:22px"><sup style="font-size:11px">$</sup>399</span>
  </div>

  <!-- Foundation -->
  <section class="service" style="top:635px">
    <div class="photo" role="img" aria-label="Cracked concrete foundation wall with a red arrow marking the crack" style="left:4px;top:4px;width:142px;height:118px;background:linear-gradient(135deg,#a8a9a2,#6d6e69 55%,#2f302d)"></div>
    <p style="left:162px;top:15px;width:306px">Advanced Foundation Review-An advanced foundation review by a licensed foundation contractor is essential when buying a home, as it provides a detailed assessment beyond what a general home inspector can offer. While home inspectors are trained generalists who identify visible issues, a foundation contractor is a specialist with the expertise to evaluate structural integrity, detect hidden problems, and determine the severity of any concerns. This specialized review can uncover issues like uneven settling, cracks, or drainage problems that may require repairs, ensuring you have a clear understanding of the foundation's condition before making a significant investment.</p>
  </section>
  <div class="tab" style="left:220px;top:618px;width:270px">ADVANCED <strong>FOUNDATION REVIEW</strong></div>
  <div class="price-burst" style="left:553px;top:657px;width:78px;height:78px">
    <svg width="78" height="78"><use href="#burst"/></svg><span style="padding-top:23px;font-size:22px"><sup style="font-size:11px">$</sup>199</span>
  </div>

  <p class="cta" style="top:779px">GET A QUOTE OR <strong>SCHEDULE AN INSPECTION TODAY!</strong></p>

  <footer class="footer">
    <div class="footer__red"></div>
    <div class="footer__phone"><span class="ico ico--phone"></span>(555) 014-2280</div>
    <div class="footer__addr"><span class="ico ico--red"></span><span>1200 Example Blvd Ste 300<br>Springdale, CA 90000</span></div>
    <div class="footer__mail"><div><span class="ico ico--red"></span>service@summitcrestinspect.com</div><div><span class="ico ico--red"></span>summitcrestinspect.com</div></div>
  </footer>
</section>

</body>
</html>
```